Infografik für Tanzschule
Zielgruppe
Wir sind eine Tanzschule für die Tänze Salsa, Bachata, kizomba & Zouk in Freiburg
Aufgabenstellung
DESIGN-BRIEFING
Tarifübersicht – Tanzschule Ritmo del Alba
Projektziel
Gestaltung einer klaren, hochwertigen Tarifübersicht für eine Tanzschule.
Die Grafik dient: als Information & Orientierung auf der Homepage, als visuelle Grundlage für das Anmeldeformular vor Ort, Der Einstieg erfolgt immer über eine gratis Schnupperstunde.
Die verbindliche Anmeldung erfolgt nach der Schnupperstunde vor Ort über ein Formular mit Auswahlkästchen.
Grundaufbau
3 Tarifkarten nebeneinander
Einheitlicher, moderner Stil
evtl. Emotionale Bilder (echte Tanzszenen, echte Menschen)
Klare Hierarchie:
Titel → Preis → Erklärung → Vorteile → Auswahlkästchen
Struktur der Tarifkarten
KARTE 1 – EINSTIEG
Titel: 1× PRO WOCHE TANZEN
Preis: 56 €/ 39 € erm.
Subline: pro Person · pro Kalendermonat
Vorteile (max. 4 Bulletpoints):
Ein fester wöchentlicher Kurs
Klare Routine & Struktur
Ausweichstunde im selben Monat möglich (muss klar enthalten sein)
Auswahl: ☐ 1× pro Woche tanzen
KARTE 2 – REGELMÄSSIG TANZEN (darf visuell leicht hervorgehoben sein, z. B. Rahmen oder Badge)
Optionales Badge:
SEHR BELIEBT
Titel: 2× PRO WOCHE TANZEN
Preis: 98 € / 68 € erm.
Vorteile:
Zwei feste wöchentliche Kurse
Mehr Praxis & schnellerer Fortschritt
Ausweichstunde im selben Monat möglich
Auswahl:
☐ 2× pro Woche tanzen
KARTE 3 – MAXIMALE FREIHEIT
Titel: FLAT – ALL YOU CAN DANCE
Preis: ab 129 € / 99 € erm.
Alle Tänze
Alle Kurse (für dein Tanz-Level)
Alle Workshops (für dein Tanz-Level)
Maximale Freiheit
☐ FLAT 1 Monat – 149 € | 119 € erm. (monatlich kündbar)
☐ FLAT 3 Monate – 129 € | 99 € erm. (3 Monate Erstlaufzeit)
Einheitlicher Hinweis unter den Karten (kleiner Text)
Ausweic..

```html
<!DOCTYPE html>
<html lang="de">
<head>
<meta charset="utf-8">
<title>Tarifübersicht – Ritmo del Alba</title>
<link href="https://fonts.googleapis.com/css2?family=Fira+Sans+Extra+Condensed:wght@700;800&family=Open+Sans:wght@400;600;700&display=swap" rel="stylesheet">
<style>
:root{
  --crimson:#b3174f;
  --card:#e6e6e6;
  --ink:#111;
  --text:#222;
  --white:#fff;
  --stage:#efefef;
  --line:#555;
  --head:"Fira Sans Extra Condensed", "Arial Narrow", sans-serif;
  --body:"Open Sans", Arial, sans-serif;
}
*{margin:0;padding:0;box-sizing:border-box}
html,body{width:1200px;height:675px;overflow:hidden}
body{position:relative;background:var(--white);font-family:var(--body);color:var(--text)}

.stage-right{position:absolute;left:724px;top:0;width:476px;height:675px;background:var(--stage)}

.tariff-board{position:absolute;width:610px;height:465px}
.tariff-board--web{left:57px;top:118px}
.tariff-board--form{left:27px;top:155px;transform:scale(.524);transform-origin:0 0}

.photo{position:absolute}
.photo--couple{left:427px;top:12px;width:182px;height:151px;background:linear-gradient(135deg,#e9e3dc 0%,#b8a89a 45%,#3a2f2b 70%,#d9c7b5 100%)}
.photo--red{left:0;top:163px;width:183px;height:165px;background:linear-gradient(120deg,#c9762e 0%,#b52a2a 40%,#e7d2bd 70%,#7a5a3a 100%)}
.photo--spin{left:396px;top:328px;width:213px;height:135px;background:linear-gradient(110deg,#5a3a2a 0%,#d59a6a 35%,#b8a0d0 65%,#8a6ab0 100%)}

.card{position:absolute;width:426px;background:var(--card);border-radius:19px}
.card--entry{left:31px;top:0;height:143px}
.card--regular{left:153px;top:152px;height:142px}
.card--flat{left:31px;top:302px;height:150px}

.card__title{position:absolute;left:13px;top:9px;font-family:var(--head);font-weight:700;color:var(--crimson);font-size:21px;line-height:1.05}

.benefits{position:absolute;list-style:none;display:flex;flex-direction:column;font-size:10.5px;line-height:12px;color:var(--text)}
.card--entry .benefits{left:213px;top:13px;gap:6px}
.card--regular .benefits{left:212px;top:12px;gap:8px}
.card--flat .benefits{left:244px;top:14px;gap:6px}
.benefits li{position:relative;padding-left:24px}
.benefits li::before{content:"";position:absolute;left:0;top:0;width:12px;height:12px;border-radius:50%;background:var(--crimson)}
.benefits li::after{content:"";position:absolute;left:3.5px;top:2.5px;width:5px;height:3px;border-left:1.8px solid var(--white);border-bottom:1.8px solid var(--white);transform:rotate(-45deg)}

.price{position:absolute;display:flex;align-items:baseline;gap:8px}
.card--entry .price{left:213px;top:86px}
.card--regular .price{left:212px;top:87px}
.card--flat .price{left:244px;top:92px}
.price__amount{font-family:var(--head);font-weight:800;font-size:40px;line-height:1;color:var(--ink)}
.price__unit{font-size:10.5px}
.price__reduced{position:absolute;font-size:9px}
.card--entry .price__reduced{left:213px;top:120px}
.card--regular .price__reduced{left:212px;top:123px}
.card--flat .price__reduced{left:244px;top:129px}

.option{position:absolute;left:13px;width:152px;height:26px;background:var(--white);border-radius:13px;display:flex;align-items:center;padding-left:15px;gap:12px;font-size:10px}
.card--entry .option{top:104px}
.card--regular .option{top:103px}
.option--wide{width:200px;height:34px;border-radius:17px;line-height:11px}
.card--flat .option--month{top:60px}
.card--flat .option--quarter{top:103px}
.option__radio{flex:none;width:12px;height:12px;border:1px solid var(--ink);border-radius:50%}
.option small{font-size:8.5px;display:block}

.badge{position:absolute;left:543px;top:243px;width:72px;height:72px;border-radius:50%;background:var(--white);display:flex;align-items:center;justify-content:center}
.badge__disc{width:60px;height:60px;border-radius:50%;background:var(--crimson);display:flex;align-items:center;justify-content:center;color:var(--white);font-family:var(--head);font-weight:700;font-size:12px;line-height:1;text-align:center;transform:rotate(-13deg)}

.form-sheet{position:absolute;left:776px;top:74px;width:372px;height:526px;background:var(--white);font-size:5px;color:var(--ink)}
.form-sheet__title{position:absolute;left:26px;top:19px;font-family:var(--head);font-weight:800;font-size:21px;color:var(--ink)}
.form-sheet__brand{position:absolute;left:267px;top:21px;display:flex;align-items:center;gap:4px;font-size:8px;font-weight:600;color:var(--crimson)}
.form-sheet__brand i{width:6px;height:6px;border-radius:50%;background:var(--crimson)}
.fields{position:absolute;left:26px;top:53px;width:212px}
.field{height:16.3px;border-bottom:.6px solid var(--line);line-height:6px}
.address{position:absolute;left:267px;top:51px;line-height:6.2px}
.address b{display:block}
.address p{margin-bottom:3.5px}
.consent{position:absolute;top:138px;display:flex;align-items:center;gap:5px}
.consent i{width:6px;height:6px;border:.6px solid var(--ink);border-radius:50%}
.consent--reduced{left:27px}
.consent--news{left:174px}
.sepa{position:absolute;left:26px;top:409px;width:320px}
.sepa h2{font-size:5.2px;font-weight:600}
.sepa p{font-size:3.3px;line-height:4px;margin-top:1px}
.bank{position:absolute;left:26px;width:320px;height:10px;border-bottom:.6px solid var(--line)}
.bank--institute{top:437px}
.bank--iban{top:453px}
.start{position:absolute;left:26px;top:471px}
.months{display:flex;margin-top:5px}
.month{width:12.3px;font-size:3.6px;display:flex;flex-direction:column;gap:3px}
.month i{width:6px;height:6px;border:.6px solid var(--ink)}
.signature{position:absolute;left:186px;top:471px;width:160px;height:25px;border-bottom:.6px solid var(--line)}
.signature small{display:block;font-size:3px;color:#777;margin-top:3px}
.terms{position:absolute;left:26px;top:508px;width:320px;font-size:3px;white-space:nowrap}
</style>
</head>
<body>
<div class="stage-right"></div>

<section class="tariff-board tariff-board--web">
  <div class="photo photo--couple" role="img" aria-label="Foto: Tanzpaar beim Paartanz im Kursraum"></div>
  <div class="photo photo--red" role="img" aria-label="Foto: lachendes Paar beim Salsa tanzen"></div>
  <div class="photo photo--spin" role="img" aria-label="Foto: Tänzerin bei einer Drehung mit Partner"></div>

  <article class="card card--entry">
    <h2 class="card__title">Einstieg:<br>Mache den ersten<br>Schritt.</h2>
    <ul class="benefits">
      <li>Ein fester wöchentlicher Kurs</li>
      <li>Klare Routine &amp; Struktur</li>
      <li>Ausweichstunde im selben<br>Monat möglich</li>
    </ul>
    <div class="price"><span class="price__amount">56 €</span><span class="price__unit">pro Person/Monat</span></div>
    <p class="price__reduced">39 € ermäßigt pro Person/Monat</p>
    <div class="option"><span class="option__radio"></span>1× pro Woche tanzen</div>
  </article>

  <article class="card card--regular">
    <h2 class="card__title">Regelmäßig:<br>Finde<br>deine Passion.</h2>
    <ul class="benefits">
      <li>Zwei feste wöchentliche Kurse</li>
      <li>Mehr Praxis &amp; schnellerer Fortschritt</li>
      <li>Ausweichstunde im selben<br>Monat möglich</li>
    </ul>
    <div class="price"><span class="price__amount">98 €</span><span class="price__unit">pro Person/Monat</span></div>
    <p class="price__reduced">68 € ermäßigt pro Person/Monat</p>
    <div class="option"><span class="option__radio"></span>2× pro Woche tanzen</div>
  </article>

  <article class="card card--flat">
    <h2 class="card__title">Maximale Freiheit:<br>All you can dance.</h2>
    <ul class="benefits">
      <li>Alle Tänze</li>
      <li>Alle Kurse&nbsp; (für dein Tanz-Level)</li>
      <li>Alle Workshops<br>(für dein Tanz-Level)</li>
    </ul>
    <div class="price"><span class="price__amount">129 €</span><span class="price__unit">pro Person/Monat</span></div>
    <p class="price__reduced">99 € ermäßigt pro Person/Monat</p>
    <div class="option option--wide option--month"><span class="option__radio"></span><span>FLAT 1 Monat 149 €<small>119 € ermäßigt / monatlich kündbar</small></span></div>
    <div class="option option--wide option--quarter"><span class="option__radio"></span><span>FLAT 3 Monate 129 €<small>99 € ermäßigt / 3 Monate Erstlaufzeit</small></span></div>
  </article>

  <div class="badge"><div class="badge__disc">SEHR<br>BELIEBT</div></div>
</section>

<section class="form-sheet">
  <h1 class="form-sheet__title">Anmeldeformular</h1>
  <div class="form-sheet__brand"><i></i>Ritmo del Alba</div>

  <div class="fields">
    <div class="field">Vor- &amp; Nachname:</div>
    <div class="field">Straße, Nr.:</div>
    <div class="field">Plz, Ort:</div>
    <div class="field">Telefon:</div>
    <div class="field">E-Mail:</div>
  </div>

  <div class="address">
    <p><b>Tanzschule Ritmo del Alba</b>Lindenweg 14<br>79100 Freiburg im Breisgau</p>
    <p><b>Geschäftsanschrift</b>Jonas Weber<br>Ahornstraße 9<br>79106 Freiburg im Breisgau</p>
    <p><b>Kontakt</b>0152 11 482 306<br>info@ritmo-del-alba.de<br>ritmo-del-alba.de</p>
  </div>

  <div class="consent consent--reduced"><i></i>Ermäßigt (Student*in / Schüler*in / Auszubildende*r)</div>
  <div class="consent consent--news"><i></i>Ja, ich möchte den Newsletter und Kursinformationen erhalten.</div>

  <section class="tariff-board tariff-board--form">
    <div class="photo photo--couple" role="img" aria-label="Foto: Tanzpaar beim Paartanz im Kursraum"></div>
    <div class="photo photo--red" role="img" aria-label="Foto: lachendes Paar beim Salsa tanzen"></div>
    <div class="photo photo--spin" role="img" aria-label="Foto: Tänzerin bei einer Drehung mit Partner"></div>

    <article class="card card--entry">
      <h2 class="card__title">Einstieg:<br>Mache den ersten<br>Schritt.</h2>
      <ul class="benefits">
        <li>Ein fester wöchentlicher Kurs</li>
        <li>Klare Routine &amp; Struktur</li>
        <li>Ausweichstunde im selben<br>Monat möglich</li>
      </ul>
      <div class="price"><span class="price__amount">56 €</span><span class="price__unit">pro Person/Monat</span></div>
      <p class="price__reduced">39 € ermäßigt pro Person/Monat</p>
      <div class="option"><span class="option__radio"></span>1× pro Woche tanzen</div>
    </article>

    <article class="card card--regular">
      <h2 class="card__title">Regelmäßig:<br>Finde<br>deine Passion.</h2>
      <ul class="benefits">
        <li>Zwei feste wöchentliche Kurse</li>
        <li>Mehr Praxis &amp; schnellerer Fortschritt</li>
        <li>Ausweichstunde im selben<br>Monat möglich</li>
      </ul>
      <div class="price"><span class="price__amount">98 €</span><span class="price__unit">pro Person/Monat</span></div>
      <p class="price__reduced">68 € ermäßigt pro Person/Monat</p>
      <div class="option"><span class="option__radio"></span>2× pro Woche tanzen</div>
    </article>

    <article class="card card--flat">
      <h2 class="card__title">Maximale Freiheit:<br>All you can dance.</h2>
      <ul class="benefits">
        <li>Alle Tänze</li>
        <li>Alle Kurse&nbsp; (für dein Tanz-Level)</li>
        <li>Alle Workshops<br>(für dein Tanz-Level)</li>
      </ul>
      <div class="price"><span class="price__amount">129 €</span><span class="price__unit">pro Person/Monat</span></div>
      <p class="price__reduced">99 € ermäßigt pro Person/Monat</p>
      <div class="option option--wide option--month"><span class="option__radio"></span><span>FLAT 1 Monat 149 €<small>119 € ermäßigt / monatlich kündbar</small></span></div>
      <div class="option option--wide option--quarter"><span class="option__radio"></span><span>FLAT 3 Monate 129 €<small>99 € ermäßigt / 3 Monate Erstlaufzeit</small></span></div>
    </article>

    <div class="badge"><div class="badge__disc">SEHR<br>BELIEBT</div></div>
  </section>

  <div class="sepa">
    <h2>Einzugsermächtigung / SEPA-Lastschriftmandat</h2>
    <p>Ich ermächtige Ritmo del Alba, Zahlungen von meinem Konto per Lastschrift einzuziehen, und weise mein Kreditinstitut an, diese Lastschriften einzulösen. Bei Ablehnung der Lastschrift fallen Kosten von 10,00 € pro Rückbuchung an. Ich kann innerhalb von acht Wochen ab Belastungsdatum die Erstattung verlangen. Es gelten die Bedingungen meines Kreditinstituts. Die Kursgebühr wird im ersten Monat zur Mitte/Ende eingezogen, danach jeweils zum 05. jedes Monats.</p>
  </div>
  <div class="bank bank--institute">Kreditinsitut:</div>
  <div class="bank bank--iban">IBAN:</div>

  <div class="start">Kursstart / Anmeldung ab:
    <div class="months">
      <span class="month">Jan<i></i></span><span class="month">Feb<i></i></span><span class="month">Mrz<i></i></span><span class="month">Apr<i></i></span><span class="month">Mai<i></i></span><span class="month">Jun<i></i></span><span class="month">Jul<i></i></span><span class="month">Aug<i></i></span><span class="month">Sep<i></i></span><span class="month">Okt<i></i></span><span class="month">Nov<i></i></span><span class="month">Dez<i></i></span>
    </div>
  </div>
  <div class="signature">Datum / Unterschrift:<small>Wir verweisen auf unsere umseitig abgedruckten AGB</small></div>

  <p class="terms">Verlängerung &amp; Kündigung: Der Vertrag verlängert sich automatisch um jeweils einen Monat und ist mit 14 Tagen Frist zum Monatsende kündbar. Ausnahme „FLAT 3 Monate“ kündbar nach Ablauf der Erstlaufzeit.</p>
</section>
</body>
</html>
```